Kessel Fahrwerkstatt
Sehr angenehme zusammenarbeit nicht aufdringlich und genau auf die Wünsche eingegangen. Wir werde sicher noch mehr zusammen Arbeiten. Gruss Lukas Hemmerle Inhaber Kessel Fahrwerkstatt
Zielgruppe
Dinks und Kunden mit viel Erfolg und hohem Ausgabepotential.
Aufgabenstellung
Unsere Firma vertreibt Fahrzeuge im Luxusbereich hauptgebiet Valtro aber auch andere Sportwagen. Was uns fehlt ist ein optischer Wiedererkennugswert. Deshalb hätten wir gerne ein Visitenkarten Design und Briefpapier Design. Später soll auch noch eine Webseite mit gleichem Wiedererkennungswert entstehen. " Roter Faden "

```html
<!DOCTYPE html>
<html lang="de">
<head>
<meta charset="utf-8">
<title>Kessel Fahrwerkstatt – Geschäftsausstattung</title>
<link rel="stylesheet" href="https://fonts.googleapis.com/css2?family=Source+Sans+3:wght@300;400;600&display=swap">
<style>
  :root {
    --backdrop: #e8e3dc;
    --paper: #ffffff;
    --gold: #c9994b;
    --gold-light: #e7c88c;
    --gold-dark: #a67630;
    --navy: #1b2956;
    --navy-deep: #121c3e;
    --ink: #3a3a3a;
    --ink-soft: #8c8c8c;
    --ink-faint: #b4b4b4;
    --signature: #1f3aa8;
  }
  * { box-sizing: border-box; margin: 0; padding: 0; }
  html, body {
    width: 1200px; height: 800px; overflow: hidden;
    background: var(--backdrop);
    font-family: "Source Sans 3", "Myriad Pro", Arial, sans-serif;
    color: var(--ink);
  }
  .stage { position: relative; width: 1200px; height: 800px; }

  .piece { position: absolute; }
  .piece-shape { position: absolute; inset: 0; width: 100%; height: 100%; }
  .letterhead .piece-shape { filter: drop-shadow(0 3px 6px rgba(0,0,0,.18)); }
  .card .piece-shape { filter: drop-shadow(0 2px 4px rgba(0,0,0,.2)); }

  /* brand name block */
  .brand { position: absolute; display: flex; align-items: center; gap: 8px; color: var(--gold); font-weight: 400; }
  .brand-dot { border-radius: 50%; background: var(--gold); flex: none; }
  .brand-name { text-transform: uppercase; line-height: 1.05; letter-spacing: .08em; }

  /* letterhead */
  .letterhead { left: 513px; top: 30px; width: 647px; height: 740px; }
  .letterhead .brand { left: 284px; top: 92px; }
  .letterhead .brand-dot { width: 30px; height: 30px; }
  .letterhead .brand-name { font-size: 17px; }

  .recipient { position: absolute; left: 63px; top: 166px; font-size: 8px; font-weight: 600; line-height: 1.35; }
  .sender { position: absolute; left: 316px; top: 166px; font-size: 7px; line-height: 1.4; color: var(--ink-soft); }
  .sender strong { color: var(--ink); font-weight: 600; }
  .sender .gap { height: 9px; }

  .letter-body { position: absolute; left: 63px; top: 291px; width: 350px; font-size: 7.2px; line-height: 1.45; color: var(--ink); }
  .letter-body p { margin-bottom: 9px; }
  .letter-body .salutation { margin-bottom: 17px; }
  .closing { position: absolute; left: 63px; top: 499px; font-size: 7.2px; }
  .signature { position: absolute; left: 63px; top: 517px; width: 84px; height: 46px;
    background: linear-gradient(100deg, rgba(31,58,168,.0), rgba(31,58,168,.25) 40%, rgba(31,58,168,.1)); border-radius: 4px; }

  .letter-footer { position: absolute; left: 63px; top: 686px; width: 540px; display: flex; font-size: 6.4px; line-height: 1.45; color: var(--ink-faint); }
  .letter-footer .footer-contact { width: 224px; }
  .letter-footer .footer-bank { border-left: 1px solid #d4d4d4; padding-left: 12px; margin-top: -8px; padding-top: 8px; height: 40px; }

  /* business cards */
  .card { left: 237px; width: 214px; height: 127px; }
  .card-front { top: 340px; }
  .card-back { top: 490px; }
  .card .brand { left: 26px; top: 48px; gap: 6px; }
  .card .brand-dot { width: 18px; height: 18px; }
  .card .brand-name { font-size: 11px; }
  .card-contact { position: absolute; left: 10px; bottom: 12px; font-size: 4.6px; line-height: 1.5; color: #8f98b8; }
  .card-back .brand { top: 62px; }
</style>
</head>
<body>
<main class="stage">

  <!-- Business card, front -->
  <section class="piece card card-front" aria-label="Visitenkarte Vorderseite">
    <svg class="piece-shape" viewBox="0 0 214 127" preserveAspectRatio="none" aria-hidden="true">
      <defs>
        <linearGradient id="cardGold" x1="0" x2="1">
          <stop offset="0" stop-color="var(--gold-dark)"/>
          <stop offset=".6" stop-color="var(--gold-light)"/>
          <stop offset="1" stop-color="var(--gold)"/>
        </linearGradient>
        <linearGradient id="cardNavy" x1="0" y1="0" x2="1" y2="1">
          <stop offset="0" stop-color="#2a3a70"/>
          <stop offset="1" stop-color="var(--navy-deep)"/>
        </linearGradient>
      </defs>
      <path d="M0,22 C60,20 110,18 134,14 C150,11 152,2 174,2 C194,2 205,5 214,8 L214,127 L0,127 Z" fill="url(#cardGold)"/>
      <path d="M0,25 C60,23 110,21 134,17 C150,14 152,5 174,5 C194,5 205,8 214,11 L214,127 L0,127 Z" fill="url(#cardNavy)"/>
    </svg>
    <div class="brand">
      <span class="brand-dot"></span>
      <span class="brand-name">Kessel<br>Fahrwerkstatt</span>
    </div>
    <address class="card-contact" style="font-style:normal">
      Marlene Fährmann | Geschäftsführerin<br>
      Werkstraße 12 | 72390 Ostheimen | Tel. +49 (0)7431 558120<br>
      Mobil +49 (0)171 4402931 | Fax +49 (0)7431 558129 | info@kessel-fahrwerkstatt.de
    </address>
  </section>

  <!-- Business card, back -->
  <section class="piece card card-back" aria-label="Visitenkarte Rückseite">
    <svg class="piece-shape" viewBox="0 0 214 127" preserveAspectRatio="none" aria-hidden="true">
      <path d="M0,22 C60,20 110,18 134,14 C150,11 152,2 174,2 C194,2 205,5 214,8 L214,127 L0,127 Z" fill="url(#cardGold)"/>
      <path d="M0,25 C60,23 110,21 134,17 C150,14 152,5 174,5 C194,5 205,8 214,11 L214,127 L0,127 Z" fill="var(--paper)"/>
    </svg>
    <div class="brand">
      <span class="brand-dot"></span>
      <span class="brand-name">Kessel<br>Fahrwerkstatt</span>
    </div>
  </section>

  <!-- Letterhead -->
  <article class="piece letterhead" aria-label="Briefbogen">
    <svg class="piece-shape" viewBox="0 0 647 740" preserveAspectRatio="none" aria-hidden="true">
      <defs>
        <linearGradient id="letterGold" x1="0" x2="1">
          <stop offset="0" stop-color="var(--gold-dark)"/>
          <stop offset=".55" stop-color="var(--gold-light)"/>
          <stop offset="1" stop-color="var(--gold)"/>
        </linearGradient>
      </defs>
      <path d="M0,48 C120,46 200,44 235,40 C265,36 272,10 330,8 C450,4 560,12 647,24 L647,740 L0,740 Z" fill="url(#letterGold)"/>
      <path d="M0,55 C120,53 200,51 235,47 C265,43 272,17 330,15 C450,11 560,19 647,31 L647,740 L0,740 Z" fill="var(--paper)"/>
    </svg>

    <div class="brand">
      <span class="brand-dot"></span>
      <span class="brand-name">Kessel<br>Fahrwerkstatt</span>
    </div>

    <address class="recipient" style="font-style:normal">
      Jonas Beispielmann<br>
      Ahornweg 7<br>
      54321 Tannried
    </address>

    <address class="sender" style="font-style:normal">
      <strong>Marlene Fährmann</strong><br>
      <strong>Geschäftsführerin</strong>
      <div class="gap"></div>
      Werkstraße 12<br>
      72390 Ostheimen
      <div class="gap"></div>
      Tel. +49 (0)7431 558120<br>
      Mobil +49 (0)171 4402931<br>
      Fax +49 (0)7431 558129<br>
      E-Mail info@kessel-fahrwerkstatt.de
    </address>

    <div class="letter-body">
      <p class="salutation">Sehr geehrte Damen und Herren,</p>
      <p>Vielen Dank für Ihr Interesse an unseren Fahrzeugen. Gerne stellen wir Ihnen unser aktuelles Angebot an Sportwagen vor und beraten Sie persönlich in unserem Haus. Jedes Modell wird vor der Übergabe sorgfältig geprüft und gepflegt.</p>
      <p>Unsere Werkstatt betreut Ihr Fahrzeug über den Kauf hinaus. Wartung, Fahrwerksabstimmung und Pflege übernehmen erfahrene Techniker, die jedes Detail kennen. Auf Wunsch holen wir Ihren Wagen ab und bringen ihn nach dem Termin zurück. So bleibt Ihnen mehr Zeit für das Wesentliche. Gerne vereinbaren wir eine Probefahrt zu einem Termin, der Ihnen passt, und zeigen Ihnen die Besonderheiten jedes Modells in Ruhe vor Ort.</p>
      <p>Für Rückfragen stehen wir Ihnen jederzeit zur Verfügung. Sie erreichen uns telefonisch, per E-Mail oder direkt in unserem Ausstellungsraum. Wir freuen uns darauf, Sie bald bei uns begrüßen zu dürfen und gemeinsam das passende Fahrzeug für Sie zu finden. Auch Inzahlungnahmen und Finanzierungen besprechen wir gerne mit Ihnen.</p>
    </div>

    <p class="closing">Mit freundlichen Grüßen</p>
    <div class="signature" role="img" aria-label="Handschriftliche Unterschrift in blauer Tinte"></div>

    <footer class="letter-footer">
      <div class="footer-contact">
        Marlene Fährmann | Geschäftsführerin<br>
        Werkstraße 12 | 72390 Ostheimen | Tel. +49 (0)7431 558120<br>
        Mobil +49 (0)171 4402931 | Fax +49 (0)7431 558129 | info@kessel-fahrwerkstatt.de
      </div>
      <div class="footer-bank">
        Bankverbindung: Kreissparkasse Ostheimen<br>
        Konto-Nr. 0 118 402 756 | BLZ 600 512 00
      </div>
    </footer>
  </article>

</main>
</body>
</html>
```